Dorvelan Swimming & Athletics Center

We need Business Card for a Athletics center
The logo frome the Uploaded Files ( b card fimal)
Οn one side of card we need the logo of company the Contact and the website:
1. Address:(Limassol, Cyprus 12-14 Stavrinelou str,Ano Trimeni,P.C. 4832)

2.Phone number: (+357) 25-704263

3. Mail: info@dorvelanfit.example

3. Website: www.dorvelanfit.example

Οn the other side of the card we need to write the sport of the company:

1. Artistic Gymnastics
2. Swimming
3. Gym - Fitness
4. Programs
5. Dancing
5.Tennis

From the Uploaded Files you can get the logo.In a logo is behind the black color which can be removed from logo.

Υou can use that color you want.
.
Updates

Industry/Entity Type

Business

Font styles to use
Decorative

Colors
0555a3
ffcf3e
3176b5
0692cd
add136
f04a50
000000
cfcfcf
9d9d9d

Requirements
Should not have
• photos with faces
• photo fro the Website:www.dorvelanfit.example

```html
<!DOCTYPE html>
<html lang="en">
<head>
<meta charset="utf-8">
<title>Dorvelan Athletics Center – Business Card</title>
<link rel="stylesheet" href="https://fonts.googleapis.com/css2?family=Open+Sans:wght@400;600;800&display=swap">
<style>
  :root {
    --page-bg: #e9e7e4;
    --card-dark: #1b1c21;
    --card-dark-edge: #111216;
    --gold: #f7b82c;
    --gold-light: #ffcf3e;
    --gold-deep: #f2a91f;
    --text-light: #ffffff;
    --text-dark: #1b1c21;
  }
  * { margin: 0; padding: 0; box-sizing: border-box; }
  html, body {
    width: 1200px;
    height: 900px;
    overflow: hidden;
    background: var(--page-bg);
    font-family: "Open Sans", Arial, sans-serif;
  }
  .business-card {
    position: absolute;
    left: 160px;
    top: 180px;
    width: 880px;
    height: 540px;
    border-radius: 24px;
    overflow: hidden;
    background: linear-gradient(180deg, var(--card-dark) 0%, var(--card-dark-edge) 100%);
    box-shadow: 0 14px 40px rgba(0, 0, 0, 0.18);
  }
  .brand {
    position: absolute;
    top: 52px;
    left: 0;
    width: 100%;
    display: flex;
    justify-content: center;
    align-items: center;
    gap: 30px;
    padding-left: 80px;
  }
  .brand-name {
    font-weight: 800;
    font-size: 88px;
    letter-spacing: 2px;
    line-height: 1;
    color: var(--gold);
  }
  .brand-mark {
    width: 118px;
    height: 118px;
    border-radius: 50%;
    border: 4px solid var(--gold-light);
    background: var(--card-dark-edge);
  }
  .contact-icons {
    position: absolute;
    top: 208px;
    left: 0;
    width: 100%;
    display: flex;
    justify-content: center;
    gap: 12px;
  }
  .contact-icons svg { width: 20px; height: 20px; fill: var(--gold); }
  .contact-list {
    position: absolute;
    top: 236px;
    left: 0;
    width: 100%;
    text-align: center;
    list-style: none;
    color: var(--text-light);
    font-size: 23px;
    line-height: 32px;
  }
  .center-name {
    position: absolute;
    top: 350px;
    left: 0;
    width: 100%;
    text-align: center;
    color: var(--gold);
    font-weight: 600;
    font-size: 23px;
  }
  .center-address {
    position: absolute;
    top: 382px;
    left: 0;
    width: 100%;
    text-align: center;
    color: var(--text-light);
    font-size: 23px;
  }
  .sports-band {
    position: absolute;
    left: 0;
    bottom: 0;
    width: 100%;
    height: 104px;
    display: flex;
    align-items: center;
    justify-content: center;
    background: linear-gradient(180deg, var(--gold-light) 0%, var(--gold-deep) 100%);
    color: var(--text-dark);
    font-size: 24px;
  }
</style>
</head>
<body>
  <div class="business-card">
    <div class="brand">
      <span class="brand-name">DORVELAN</span>
      <span class="brand-mark"></span>
    </div>

    <div class="contact-icons" aria-hidden="true">
      <svg viewBox="0 0 20 20" class="icon-phone"><path d="M3 7c0-2 2-3 7-3s7 1 7 3v2h-4V7.5c-1-.5-5-.5-6 0V9H3z M6 10h8l2 6H4z"/></svg>
      <svg viewBox="0 0 20 20" class="icon-mail"><path d="M2 5h16v10H2z" /><path d="M2 5l8 6 8-6" fill="none" stroke="#1b1c21" stroke-width="1.6"/></svg>
      <svg viewBox="0 0 20 20" class="icon-globe"><circle cx="10" cy="10" r="8"/><path d="M10 2c-3 3-3 13 0 16M10 2c3 3 3 13 0 16M2 10h16" fill="none" stroke="#1b1c21" stroke-width="1.4"/></svg>
    </div>

    <ul class="contact-list">
      <li>(+357) 25-704263</li>
      <li>info@dorvelanfit.example</li>
      <li>www.dorvelanfit.example</li>
    </ul>

    <p class="center-name">DORVELAN ATHLETICS CENTER</p>
    <p class="center-address">Limassol, Cyprus 12-14 Stavrinelou str, Ano Trimeni,P.C. 4832</p>

    <div class="sports-band">
      Artistic Gymnastics | Swimming | Gym - Fitness | Programs | Dancing Tennis
    </div>
  </div>
</body>
</html>
```